The RVH Relational Philanthropy Cycle

The title for this graphic is above. It must be included.
I am looking for a graphic representation of the relationship between the Christian school and the donor / pointing to the child (student) - the school's mission / outcome of investment through a gift / appreciation of the gift / communication of the gift impact for the child / stronger relationship going back to the child. This is not easy to do. I've tried to do it on my own and can't get it.
Any cliched child representations will be dismissed out of hand e.g. mortar boards, pencils, uniforms etc. The child should be abstract so that gender and race are irrelevant.
The key to this whole thing is the idea of RELATIONSHIP. The close relationship of donor and the Christian school, the pointing of that relationship to focus on the child / the school's mission, the outpouring of generosity that then happens in the heart of the donor and the gift that results, followed up by intentional work by the Christian school to thank and inform the donor - thank for the gift inform about the gift's expenditure and impact in the life of the child - all of which leads to a strengthening of the relationship and continued philanthropy as a never ending cycle.
It must be branded - logo and colors attached.
It must be obvious - easy to grasp the basic idea of relationship resulting in generosity / philanthropy. The visual should be clear - any words used illustrate - I should not 'need' the words to understand the idea.
I need it on a PP slide, jpeg, thumbnail. It must be highly legible in no more than 1/3 of a regular size piece of paper.
Our website is brightfieldacademyguild.org
google donor cultivation cycle or donor giving cycle to see many examples of cycles that are used in secular contexts - the big difference in RVH's is the focus on the child and the importance of the relationship.

```html
<!DOCTYPE html>
<html lang="en">
<head>
<meta charset="utf-8">
<title>The RVH Relational Philanthropy Cycle</title>
<link rel="stylesheet" href="https://fonts.googleapis.com/css2?family=EB+Garamond:wght@500&family=Montserrat:wght@400;500;700&display=swap">
<style>
  :root {
    --page: #f5f5f5;
    --card: #ffffff;
    --brand-blue: #4475a8;
    --brand-blue-dark: #3a6699;
    --title-grey: #7d7d7d;
    --arrow-grey: #919191;
    --ring-grey: #d9d9d9;
    --ring-blue: #87a9cf;
    --donor-orange: #eea445;
    --steward-green: #6aae45;
    --label-grey: #7a7a7a;
    --ink: #3a3a3a;
    --white: #ffffff;
  }
  * { margin: 0; padding: 0; box-sizing: border-box; }
  html, body { width: 820px; height: 1200px; overflow: hidden; background: var(--page); }
  .canvas { position: relative; width: 820px; height: 1200px; }
  .slide { position: absolute; left: 29px; width: 762px; height: 552px; background: var(--card); }
  .slide--mono { top: 24px; }
  .slide--colour { top: 606px; }
  .slide svg { display: block; width: 762px; height: 552px; }
  .title { font-family: "EB Garamond", Georgia, serif; font-size: 25px; font-weight: 500; fill: var(--title-grey); }
  .title .title-brand { fill: var(--brand-blue); }
  .arc-label { font-family: "Montserrat", Arial, sans-serif; font-size: 14px; font-weight: 500; letter-spacing: .3px; }
  .verse { font-family: "Montserrat", Arial, sans-serif; font-size: 14px; font-weight: 500; }
  .node-label { font-family: "Montserrat", Arial, sans-serif; font-size: 13.5px; font-weight: 700; fill: var(--white); }
  .copyright { font-family: "Montserrat", Arial, sans-serif; font-size: 12.5px; font-weight: 500; fill: var(--ink); }
  .brand-name { font-family: "Montserrat", Arial, sans-serif; font-size: 30px; font-weight: 500; fill: var(--brand-blue); }
  .icon { fill: none; stroke: var(--white); stroke-width: 1.8; stroke-linecap: round; stroke-linejoin: round; }
</style>
</head>
<body>
<div class="canvas">

  <!-- Grey-arrow version -->
  <section class="slide slide--mono">
    <svg viewBox="0 0 790 572" role="img" aria-label="The RVH Relational Philanthropy Cycle">
      <defs>
        <symbol id="icon-heart-hand" viewBox="-20 -20 40 40">
          <path class="icon" d="M0 -2 C-9 -8 -9 -17 -4 -17 C-2 -17 -1 -15 0 -13 C1 -15 2 -17 4 -17 C9 -17 9 -8 0 -2 Z"/>
          <path class="icon" d="M-17 6 L-11 3 C-8 2 -5 3 -2 5 L4 5 C6 5 6 8 4 8 L-3 8 M4 8 L11 3 C13 2 15 4 13 6 L6 13 C4 14 2 15 0 15 L-10 15 L-17 18"/>
        </symbol>
        <symbol id="icon-child" viewBox="-20 -20 40 40">
          <circle class="icon" cx="-9" cy="-12" r="3"/>
          <circle class="icon" cx="0" cy="-15" r="3.3"/>
          <circle class="icon" cx="9" cy="-12" r="3"/>
          <rect class="icon" x="-12.5" y="-6" width="7" height="20" rx="3.5"/>
          <rect class="icon" x="-4" y="-9" width="8" height="24" rx="4"/>
          <rect class="icon" x="5.5" y="-6" width="7" height="20" rx="3.5"/>
        </symbol>
        <symbol id="icon-gift-hand" viewBox="-20 -20 40 40">
          <circle class="icon" cx="2" cy="-8" r="7"/>
          <path class="icon" d="M-17 6 L-11 3 C-8 2 -5 3 -2 5 L4 5 C6 5 6 8 4 8 L-3 8 M4 8 L11 3 C13 2 15 4 13 6 L6 13 C4 14 2 15 0 15 L-10 15 L-17 18"/>
        </symbol>
        <symbol id="icon-globe-hand" viewBox="-20 -20 40 40">
          <circle class="icon" cx="2" cy="-8" r="8"/>
          <ellipse class="icon" cx="2" cy="-8" rx="3.5" ry="8"/>
          <path class="icon" d="M-6 -8 L10 -8 M-5 -12 L9 -12 M-5 -4 L9 -4"/>
          <path class="icon" d="M-17 6 L-11 3 C-8 2 -5 3 -2 5 L4 5 C6 5 6 8 4 8 L-3 8 M4 8 L11 3 C13 2 15 4 13 6 L6 13 C4 14 2 15 0 15 L-10 15 L-17 18"/>
        </symbol>
        <symbol id="chevrons" viewBox="-6 -6 12 12">
          <path d="M-5 -1 L1 -4 L-1 2 Z M-1 3 L5 0 L3 6 Z" fill="currentColor"/>
        </symbol>
        <path id="arc-top" d="M305 147 A182 182 0 0 1 485 147"/>
        <path id="arc-bottom" d="M284 462 A192 192 0 0 0 506 462"/>
        <path id="verse-top" d="M351.4 241.7 A76 76 0 0 1 438.6 241.7"/>
        <path id="verse-bottom" d="M345.7 374.4 A86 86 0 0 0 444.3 374.4"/>
      </defs>

      <text class="title" x="395" y="80" text-anchor="middle"><tspan class="title-brand">The RVH</tspan> Relational Philanthropy Cycle</text>

      <g class="cycle-arrows" fill="var(--arrow-grey)">
        <path d="M260.8 227.5 A155 155 0 0 1 512 203.3" fill="none" stroke="var(--arrow-grey)" stroke-width="22"/>
        <path d="M498.4 218.2 L529.1 192.5 L534.3 237.1 Z"/>
        <path d="M529.2 382.5 A155 155 0 0 1 278 406.7" fill="none" stroke="var(--arrow-grey)" stroke-width="22"/>
        <path d="M291.6 391.8 L260.9 417.5 L255.7 372.9 Z"/>
      </g>
      <text class="arc-label" fill="var(--brand-blue)"><textPath href="#arc-top" startOffset="50%" text-anchor="middle">Inspirational Giving</textPath></text>
      <text class="arc-label" fill="var(--brand-blue)"><textPath href="#arc-bottom" startOffset="50%" text-anchor="middle">Mission Based Relationship</textPath></text>

      <circle cx="395" cy="304" r="106" fill="var(--ring-grey)"/>
      <g color="var(--brand-blue)">
        <use href="#chevrons" x="322" y="245" width="12" height="12" transform="rotate(-90 328 251)"/>
        <use href="#chevrons" x="456" y="245" width="12" height="12"/>
        <use href="#chevrons" x="322" y="352" width="12" height="12" transform="rotate(180 328 358)"/>
        <use href="#chevrons" x="456" y="352" width="12" height="12" transform="rotate(90 462 358)"/>
      </g>

      <g class="node node--donor">
        <circle cx="262" cy="304" r="64" fill="var(--brand-blue)"/>
        <use href="#icon-heart-hand" x="246" y="267" width="32" height="32"/>
        <text class="node-label" x="262" y="330" text-anchor="middle">DONOR</text>
      </g>
      <g class="node node--steward">
        <circle cx="528" cy="304" r="64" fill="var(--brand-blue)"/>
        <use href="#icon-gift-hand" x="511" y="259" width="34" height="34"/>
        <text class="node-label" x="528" y="321" text-anchor="middle">DONOR</text>
        <text class="node-label" x="528" y="338" text-anchor="middle">STEWARD</text>
      </g>
      <g class="node node--child">
        <circle cx="395" cy="304" r="65" fill="var(--brand-blue)"/>
        <use href="#icon-child" x="379" y="267" width="32" height="32"/>
        <text class="node-label" x="395" y="330" text-anchor="middle">THE CHILD</text>
      </g>

      <text class="verse" fill="var(--ink)"><textPath href="#verse-top" startOffset="50%" text-anchor="middle">Luke 8:3</textPath></text>
      <text class="verse" fill="var(--ink)"><textPath href="#verse-bottom" startOffset="50%" text-anchor="middle">Mark 9:37</textPath></text>

      <text class="copyright" x="58" y="545">© Rivervale Heritage Schools 2022</text>
      <text class="brand-name" x="700" y="530" text-anchor="middle">RVH</text>
    </svg>
  </section>

  <!-- Colour version -->
  <section class="slide slide--colour">
    <svg viewBox="0 0 790 572" role="img" aria-label="The RVH Relational Philanthropy Cycle, colour version">
      <text class="title" x="395" y="80" text-anchor="middle"><tspan class="title-brand">The RVH</tspan> Relational Philanthropy Cycle</text>

      <g class="cycle-arrows" fill="var(--brand-blue)">
        <path d="M260.8 227.5 A155 155 0 0 1 512 203.3" fill="none" stroke="var(--brand-blue)" stroke-width="22"/>
        <path d="M498.4 218.2 L529.1 192.5 L534.3 237.1 Z"/>
        <path d="M529.2 382.5 A155 155 0 0 1 278 406.7" fill="none" stroke="var(--brand-blue)" stroke-width="22"/>
        <path d="M291.6 391.8 L260.9 417.5 L255.7 372.9 Z"/>
      </g>
      <text class="arc-label" fill="var(--label-grey)"><textPath href="#arc-top" startOffset="50%" text-anchor="middle">Inspirational Giving</textPath></text>
      <text class="arc-label" fill="var(--label-grey)"><textPath href="#arc-bottom" startOffset="50%" text-anchor="middle">Mission Based Relationship</textPath></text>

      <circle cx="395" cy="304" r="106" fill="var(--ring-blue)"/>
      <g color="var(--brand-blue)">
        <use href="#chevrons" x="322" y="245" width="12" height="12" transform="rotate(-90 328 251)"/>
        <use href="#chevrons" x="456" y="245" width="12" height="12"/>
        <use href="#chevrons" x="322" y="352" width="12" height="12" transform="rotate(180 328 358)"/>
        <use href="#chevrons" x="456" y="352" width="12" height="12" transform="rotate(90 462 358)"/>
      </g>

      <g class="node node--donor">
        <circle cx="262" cy="304" r="64" fill="var(--donor-orange)"/>
        <use href="#icon-heart-hand" x="246" y="267" width="32" height="32"/>
        <text class="node-label" x="262" y="330" text-anchor="middle">DONOR</text>
      </g>
      <g class="node node--steward">
        <circle cx="528" cy="304" r="64" fill="var(--steward-green)"/>
        <use href="#icon-globe-hand" x="511" y="259" width="34" height="34"/>
        <text class="node-label" x="528" y="321" text-anchor="middle">DONOR</text>
        <text class="node-label" x="528" y="338" text-anchor="middle">STEWARD</text>
      </g>
      <g class="node node--child">
        <circle cx="395" cy="304" r="66" fill="var(--brand-blue)" stroke="var(--brand-blue-dark)" stroke-width="2"/>
        <use href="#icon-child" x="379" y="267" width="32" height="32"/>
        <text class="node-label" x="395" y="330" text-anchor="middle">THE CHILD</text>
      </g>

      <text class="verse" fill="var(--white)"><textPath href="#verse-top" startOffset="50%" text-anchor="middle">Luke 8:3</textPath></text>
      <text class="verse" fill="var(--white)"><textPath href="#verse-bottom" startOffset="50%" text-anchor="middle">Mark 9:37</textPath></text>

      <text class="copyright" x="58" y="545">© Rivervale Heritage Schools 2022</text>
      <text class="brand-name" x="700" y="530" text-anchor="middle">RVH</text>
    </svg>
  </section>

</div>
</body>
</html>
```